I’m looking for a vibrant, eye-catching package design for our new premium cannabis gummies, GLIMMER. This is a high-end cannabis edible gummy made with real fruit, vegan ingredients, and powered by a THC nano emulsion — the most effective way to ingest cannabis. The package will be a square-bottom bag with child-resistant zippers (image of bag attached).

What we want from you? We want your version of what the front of the bag should look like.

The following text elements should be included within your vision of the bag

Glimmer - Premium Cannabis Gummy
10 pieces per bag | 10mg THC per piece | 100mg THC total
Made with real fruit
Vegan (include a vegan symbol)
Flavors: Assorted flavors (Strawberry, Mango, Pineapple, Orange, Blueberry)
Oregon cannabis icon (attached)
Net Weight 250 grams (bottom of bag)

What is needed after you win.
2 other sizes. Same look but will need to rearrange some elements of the bag. The back of the bag will be the same for all sizes. Will be legal text and nutritional info. Larger two sizes has sides, as per the attached bag. All sizes will have a bottom as well. the first size will have 5 versions for flavors. Other 2 sizes will be 1 design with "assorted flavors".

Target Market(s)

Cannabis market in Oregon

Industry/Entity Type

cannabis

Requirements
Must have
• the Marijuana universal icon for being a cannabis product.
Nice to have
• nice images of fruits
Should not have
• graphic, cartoon images that would appeal to minors.

```html
<!DOCTYPE html>
<html lang="en">
<head>
<meta charset="utf-8">
<title>Glimmer Premium Cannabis Gummies – Front Panel</title>
<link href="https://fonts.googleapis.com/css2?family=Exo+2:wght@400;500;600&display=swap" rel="stylesheet">
<style>
  :root {
    --ink: #0d3c45;
    --backdrop: #dcdcdc;
    --page: #ffffff;
    --panel: #ffffff;
    --blue: #3d7fb5;
    --teal-light: #a6d4cb;
    --teal-deep: #3b7e98;
    --green: #3f917b;
    --gold-dark: #c0913a;
    --gold-light: #ecd27a;
    --pill: #0f8aa0;
    --berry-red: #e30613;
    --mango: #f7a823;
    --pineapple: #a27a4a;
    --orange: #ef7d00;
    --blueberry: #951b81;
    --badge-dark: #1a1a1a;
    --badge-red: #e52421;
  }
  * { margin: 0; padding: 0; box-sizing: border-box; }
  html, body {
    width: 1200px; height: 2486px; overflow: hidden;
    background: var(--page);
    font-family: "Exo 2", sans-serif;
    color: var(--ink);
  }
  .canvas { position: relative; width: 1200px; height: 2486px; }
  .backdrop {
    position: absolute; left: 0; top: 0; width: 1200px; height: 1480px;
    background: var(--backdrop);
  }
  .front-panel {
    position: absolute; left: 166px; top: 120px; width: 885px; height: 1223px;
    background: var(--panel); overflow: hidden;
  }
  .panel-art { position: absolute; left: 0; top: 0; width: 885px; height: 1223px; }
  .abs { position: absolute; }
  .brand-name {
    left: 0; width: 100%; top: 112px; text-align: center;
    font-size: 58px; font-weight: 600; letter-spacing: 1px; padding-left: 30px;
  }
  .product-title {
    left: 0; width: 100%; top: 238px; text-align: center;
    font-size: 104px; font-weight: 500; line-height: 83px; letter-spacing: 1px;
    padding-left: 10px;
  }
  .leaf-illustration {
    left: 272px; top: 520px; width: 340px; height: 300px;
    background: radial-gradient(ellipse at 50% 55%, #f3fbf9 0%, #d7eeea 45%, rgba(166,212,203,0) 75%);
    border-radius: 50% 50% 40% 40%;
  }
  .claims {
    left: 0; width: 100%; top: 848px; text-align: center;
    font-size: 40px; line-height: 52px; padding-left: 28px;
  }
  .flavor-dots { left: 386px; top: 1039px; display: flex; gap: 12px; }
  .flavor-dots span { width: 17px; height: 17px; border-radius: 50%; display: block; }
  .flavor-list {
    left: 230px; width: 470px; top: 1072px; text-align: center;
    font-size: 23px; line-height: 29px;
  }
  .contains-label { left: 38px; top: 1047px; font-size: 15px; }
  .count-pill {
    left: 0; top: 1068px; width: 166px; height: 42px;
    background: var(--pill); color: #fff; border-radius: 0 21px 21px 0;
    padding-left: 38px; font-size: 24px; line-height: 42px;
  }
  .count-pill b { font-size: 30px; font-weight: 600; }
  .dose-total { left: 38px; top: 1110px; font-size: 22px; }
  .dose-each { left: 38px; top: 1138px; font-size: 15px; }
  .cannabis-badge { left: 767px; top: 1090px; width: 88px; height: 62px; }
</style>
</head>
<body>
<main class="canvas">
  <div class="backdrop"></div>
  <section class="front-panel">
    <svg class="panel-art" viewBox="0 0 885 1223" aria-hidden="true">
      <defs>
        <linearGradient id="skyBase" x1="0" y1="0" x2="1" y2="0">
          <stop offset="0" stop-color="var(--blue)"/>
          <stop offset="0.5" stop-color="var(--teal-light)"/>
          <stop offset="1" stop-color="var(--teal-deep)"/>
        </linearGradient>
        <radialGradient id="skyGlow" cx="0.5" cy="0.62" r="0.45">
          <stop offset="0" stop-color="#b9ddd3" stop-opacity="0.9"/>
          <stop offset="1" stop-color="#b9ddd3" stop-opacity="0"/>
        </radialGradient>
        <linearGradient id="topShade" x1="0" y1="0" x2="0" y2="1">
          <stop offset="0" stop-color="#1e6db0" stop-opacity="0.55"/>
          <stop offset="0.4" stop-color="#1e6db0" stop-opacity="0"/>
        </linearGradient>
        <linearGradient id="gold" x1="0" y1="0" x2="1" y2="0">
          <stop offset="0" stop-color="var(--gold-dark)"/>
          <stop offset="0.5" stop-color="var(--gold-light)"/>
          <stop offset="1" stop-color="var(--gold-dark)"/>
        </linearGradient>
      </defs>
      <rect width="885" height="880" fill="url(#skyBase)"/>
      <rect width="885" height="880" fill="url(#topShade)"/>
      <rect width="885" height="880" fill="url(#skyGlow)"/>
      <path d="M700 0 C560 140 540 330 640 520 C720 680 700 800 690 880 L885 880 L885 0 Z" fill="#ffffff" opacity="0.12"/>
      <path d="M840 0 C740 140 720 330 800 520 C860 660 860 780 860 880 L885 880 L885 0 Z" fill="#2d7a8f" opacity="0.25"/>
      <path d="M760 0 L885 0 L885 120 C840 60 800 30 760 0 Z" fill="var(--green)" opacity="0.5"/>
      <path d="M0 840 C240 770 640 770 885 840 L885 1223 L0 1223 Z" fill="var(--panel)"/>
      <rect y="31" width="885" height="7" fill="url(#gold)"/>
      <rect y="1193" width="885" height="7" fill="url(#gold)"/>
    </svg>

    <div class="abs brand-name">GLIMMER</div>
    <h1 class="abs product-title">PREMIUM<br>CANNABIS<br>GUMMIES</h1>
    <div class="abs leaf-illustration" role="img" aria-label="White cannabis leaf illustration"></div>

    <p class="abs claims">Real Fruit<br>Vegan</p>

    <div class="abs contains-label">CONTAINS:</div>
    <div class="abs count-pill"><b>10</b> pieces</div>
    <div class="abs dose-total">100 mg THC</div>
    <div class="abs dose-each">(10 mg THC per piece)</div>

    <div class="abs flavor-dots" aria-hidden="true">
      <span style="background:var(--berry-red)"></span>
      <span style="background:var(--mango)"></span>
      <span style="background:var(--pineapple)"></span>
      <span style="background:var(--orange)"></span>
      <span style="background:var(--blueberry)"></span>
    </div>
    <p class="abs flavor-list">ASSORTED FLAVORS:<br>Strawberry, Mango, Pineapple,<br>Orange, Blueberry</p>

    <svg class="abs cannabis-badge" viewBox="0 0 88 62" role="img" aria-label="Cannabis product warning badge">
      <rect x="1.5" y="1.5" width="85" height="59" rx="8" fill="var(--badge-dark)"/>
      <rect x="30" y="7" width="51" height="48" rx="4" fill="var(--badge-red)"/>
    </svg>
  </section>
</main>
</body>
</html>
```